依頼詳細
主にWEBサイトで販売する薬品希釈用精製水のラベルのデザイン作成依頼です。
ラベルはペットボトルにシュリンク包装します。

用途は、薬品の希釈やエタノールや塩素を希釈してアルコール消毒液や除菌剤を作る時に
使用されます。参考画像を添付します。

デザインの詳細は添付のエクセルをご参照ください。
デザインは正面の1面のみとなります。

WEB上のサムネイルで最も目に付くところで、特に「商品名」「イラスト」「特長」で
用途を一目で伝えるデザイン性を重要視します。

目的に沿ったデザインであれば、色やフォントなどは問いません。
商品名・イラスト・特長・社名・容量の配置も特に決まりはありません。

WEBに掲載した際に用途がわかりやすく、手にとっても見やすいデザインを希望します。

サイズも添付のエクセルに記載していますので、そのサイズ内での作成をお願い致します。
ペットボトルの中央にくぼみがありますので、それを利用した(上部と下部に分けた)デザインでも構いませんし、ラベルサイズ全体を利用したデザインでも構いません。

今回のサイズとは別に3種類のサイズ違い製品があります。
デザイン採用後に、デザインはそのままでリサイズのみ行っていただく作業もございます。

競合品や用途の参考となる画像も添付しますので参照とされてください。

どうぞよろしくお願いいたします。
記載項目
添付資料をご参照ください。
希望イメージ
シンプル 複雑
単色 カラフル
暗い 明るい
日常 高級
遊び心 厳粛
未来的 伝統的
女性的 男性的
希望する色
青系、水色系、紫系
納品ファイル
• 高解像度JPG (.jpg)
• イラストレーター形式 (.ai)
補足説明

商品に合ったご提案でした。

ご提案ありがとうございました。
またの機会がございましたらよろしくお願いいたします。

```html
<!DOCTYPE html>
<html lang="ja">
<head>
<meta charset="utf-8">
<title>精製水 ラベル</title>
<link href="https://fonts.googleapis.com/css2?family=Noto+Sans+JP:wght@400;500;700&display=swap" rel="stylesheet">
<style>
  :root {
    --purple: #6b4f9e;
    --purple-deep: #5a3f8c;
    --cyan: #5ec4d8;
    --cyan-light: #a8e0ea;
    --white: #ffffff;
  }
  * { margin: 0; padding: 0; box-sizing: border-box; }
  html, body { width: 1200px; height: 3000px; overflow: hidden; background: var(--white); }
  body { font-family: "Noto Sans JP", sans-serif; }
  .label { position: relative; width: 1200px; height: 3000px; overflow: hidden; background: var(--white); }

  .header-shape { position: absolute; left: 0; top: 0; width: 1200px; height: 1050px; }

  .tag {
    position: absolute; top: 88px; height: 104px;
    background: var(--cyan); color: var(--white);
    font-size: 68px; font-weight: 500; line-height: 104px; text-align: center;
    border-radius: 6px; white-space: nowrap;
  }
  .tag-category { left: 72px; width: 180px; }
  .tag-use { left: 344px; width: 800px; letter-spacing: 2px; }

  .product-name {
    position: absolute; left: 0; top: 215px; width: 1200px;
    text-align: center; color: var(--white);
    font-size: 270px; font-weight: 500; letter-spacing: 24px; line-height: 1.1;
    white-space: nowrap;
  }

  .illustration {
    position: absolute; left: 840px; top: 580px; width: 320px; height: 320px;
    border-radius: 50%; background: radial-gradient(circle at 50% 45%, #7fd0df, var(--cyan));
  }

  .feature { position: absolute; left: 0; width: 1200px; }
  .feature-badge { position: absolute; left: 66px; top: 0; width: 110px; height: 330px; }
  .feature-text { position: absolute; left: 262px; top: 0; width: 920px; }
  .feature-lead { color: var(--purple); font-size: 62px; font-weight: 400; line-height: 92px; white-space: nowrap; }
  .feature-title { color: var(--purple-deep); font-size: 88px; font-weight: 500; line-height: 130px; white-space: nowrap; }
  .feature-title-long { font-size: 80px; letter-spacing: -1px; }

  .f1 { top: 1110px; } .f2 { top: 1500px; } .f3 { top: 1890px; } .f4 { top: 2280px; }

  .footer {
    position: absolute; left: 0; top: 2660px; width: 1200px; height: 340px;
    background: var(--purple);
  }
  .company {
    position: absolute; left: 0; top: 40px; width: 1200px; text-align: center;
    color: var(--white); font-size: 66px; font-weight: 500; letter-spacing: 3px;
  }
  .volume {
    position: absolute; left: 320px; top: 172px; width: 570px; height: 110px;
    background: var(--cyan); border-radius: 10px;
  }
  .volume-label {
    position: absolute; left: 30px; top: 0; line-height: 110px;
    color: var(--white); font-size: 64px; font-weight: 500; letter-spacing: 4px;
  }
  .volume-value {
    position: absolute; left: 240px; top: 12px; width: 310px; height: 86px;
    background: var(--white); border-radius: 6px; text-align: center;
    color: var(--purple); font-size: 64px; font-weight: 500; line-height: 86px;
  }
</style>
</head>
<body>
<div class="label">
  <svg class="header-shape" viewBox="0 0 1200 1050" aria-hidden="true">
    <path d="M0 0 H1200 V560 C1000 580 820 650 600 690 C400 730 180 700 0 660 Z" fill="var(--purple)"/>
    <path d="M0 700 C200 750 420 770 600 730 C820 690 1000 620 1200 610 V660 C1000 670 820 740 600 790 C400 830 180 800 0 760 Z" fill="var(--cyan)"/>
    <path d="M0 780 C200 830 420 850 600 810 C820 770 1000 710 1200 700 V750 C1000 760 820 830 600 870 C400 910 180 880 0 840 Z" fill="var(--cyan-light)"/>
    <path d="M600 830 C565 900 545 940 545 965 A55 55 0 0 0 655 965 C655 940 635 900 600 830 Z" fill="var(--cyan)"/>
  </svg>

  <div class="tag tag-category">薬品</div>
  <div class="tag tag-use">アルコール希釈用</div>
  <h1 class="product-name">精製水</h1>

  <div class="illustration" role="img" aria-label="精製水をビーカーに注ぐイラスト"></div>

  <section class="feature f1">
    <svg class="feature-badge" viewBox="0 0 110 330" aria-hidden="true">
      <rect x="0" y="0" width="110" height="170" fill="var(--cyan)"/>
      <text x="55" y="70" fill="#fff" font-size="52" font-weight="500" text-anchor="middle" font-family="Noto Sans JP, sans-serif">特</text>
      <text x="55" y="135" fill="#fff" font-size="52" font-weight="500" text-anchor="middle" font-family="Noto Sans JP, sans-serif">長</text>
      <path d="M55 170 C30 220 5 250 5 280 A50 50 0 0 0 105 280 C105 250 80 220 55 170 Z" fill="var(--purple)"/>
      <text x="55" y="305" fill="#fff" font-size="62" font-weight="500" text-anchor="middle" font-family="Noto Sans JP, sans-serif">1</text>
    </svg>
    <div class="feature-text">
      <p class="feature-lead">薬品等の希釈に最適な</p>
      <p class="feature-lead">極めて不純物の少ない</p>
      <p class="feature-title">高純度精製水</p>
    </div>
  </section>

  <section class="feature f2">
    <svg class="feature-badge" viewBox="0 0 110 330" aria-hidden="true">
      <rect x="0" y="0" width="110" height="170" fill="var(--cyan)"/>
      <text x="55" y="70" fill="#fff" font-size="52" font-weight="500" text-anchor="middle" font-family="Noto Sans JP, sans-serif">特</text>
      <text x="55" y="135" fill="#fff" font-size="52" font-weight="500" text-anchor="middle" font-family="Noto Sans JP, sans-serif">長</text>
      <path d="M55 170 C30 220 5 250 5 280 A50 50 0 0 0 105 280 C105 250 80 220 55 170 Z" fill="var(--purple)"/>
      <text x="55" y="305" fill="#fff" font-size="62" font-weight="500" text-anchor="middle" font-family="Noto Sans JP, sans-serif">2</text>
    </svg>
    <div class="feature-text">
      <p class="feature-lead">日本産業規格</p>
      <p class="feature-lead">「JIS-K0557」における</p>
      <p class="feature-title">A2クラス相当品</p>
    </div>
  </section>

  <section class="feature f3">
    <svg class="feature-badge" viewBox="0 0 110 330" aria-hidden="true">
      <rect x="0" y="0" width="110" height="170" fill="var(--cyan)"/>
      <text x="55" y="70" fill="#fff" font-size="52" font-weight="500" text-anchor="middle" font-family="Noto Sans JP, sans-serif">特</text>
      <text x="55" y="135" fill="#fff" font-size="52" font-weight="500" text-anchor="middle" font-family="Noto Sans JP, sans-serif">長</text>
      <path d="M55 170 C30 220 5 250 5 280 A50 50 0 0 0 105 280 C105 250 80 220 55 170 Z" fill="var(--purple)"/>
      <text x="55" y="305" fill="#fff" font-size="62" font-weight="500" text-anchor="middle" font-family="Noto Sans JP, sans-serif">3</text>
    </svg>
    <div class="feature-text">
      <p class="feature-lead">薬品本来の性能を損なわず</p>
      <p class="feature-title feature-title-long">安全な調整・調合が可能</p>
    </div>
  </section>

  <section class="feature f4">
    <svg class="feature-badge" viewBox="0 0 110 330" aria-hidden="true">
      <rect x="0" y="0" width="110" height="170" fill="var(--cyan)"/>
      <text x="55" y="70" fill="#fff" font-size="52" font-weight="500" text-anchor="middle" font-family="Noto Sans JP, sans-serif">特</text>
      <text x="55" y="135" fill="#fff" font-size="52" font-weight="500" text-anchor="middle" font-family="Noto Sans JP, sans-serif">長</text>
      <path d="M55 170 C30 220 5 250 5 280 A50 50 0 0 0 105 280 C105 250 80 220 55 170 Z" fill="var(--purple)"/>
      <text x="55" y="305" fill="#fff" font-size="62" font-weight="500" text-anchor="middle" font-family="Noto Sans JP, sans-serif">4</text>
    </svg>
    <div class="feature-text">
      <p class="feature-lead">工業薬品の希釈や</p>
      <p class="feature-lead">アルコール消毒液</p>
      <p class="feature-title">除菌液の作製に</p>
    </div>
  </section>

  <footer class="footer">
    <p class="company">ソラミ化学株式会社</p>
    <div class="volume">
      <span class="volume-label">容量</span>
      <span class="volume-value">330ml</span>
    </div>
  </footer>
</div>
</body>
</html>
```